Building company buisness cards

We are looking for a sharp modern new look for our business cards.
We are a New Zealand based company that specialises in house and land packages.
We have attached a photo of the current logo and would like to see if it can be improved somehow if needed.
We are open to any colours but we have chosen green at this stage.
Feel free to change the font and make the logo smarter looking.
Play with the colours and see what looks best.

We want a card that looks so good know one will want to throw it away!

Target Market(s)

Home buyers

Industry/Entity Type

Building

Contact Information for Business Card

Dorian Keswick
0217392604
dkeswick@tidewellhomecraft.co.nz
tidewellhomecraft.co.nz

Font styles to use
Serif
Sans Serif

Colors

Designer to choose colors to be used in the design.

Requirements
Must have
• Logo and company name on one side, details on the other side
Nice to have
• Color codes for the original green are HEX #4a8028, RGB(74,128,40), CMYK(42,0,69,50)
• Round corners, Raised and/or spot UV

```html
<!DOCTYPE html>
<html lang="en">
<head>
<meta charset="utf-8">
<title>Tidewell Homecraft – Business Cards</title>
<link rel="stylesheet" href="https://fonts.googleapis.com/css2?family=Open+Sans:wght@400;500;700&display=swap">
<style>
  :root {
    --brand-green: #4a8028;
    --brand-green-light: #5a9332;
    --brand-green-dark: #3f7222;
    --card-white: #ffffff;
    --ink-grey: #4d4d4d;
    --rule-grey: #9a9a9a;
    --backdrop: #2a2a2a;
  }
  * { margin: 0; padding: 0; box-sizing: border-box; }
  html, body { width: 1200px; height: 1108px; overflow: hidden; }
  body {
    background: var(--backdrop);
    display: flex;
    align-items: center;
    justify-content: center;
    gap: 60px;
    font-family: "Open Sans", Arial, sans-serif;
  }
  .card {
    position: relative;
    width: 400px;
    height: 650px;
    border-radius: 28px;
    overflow: hidden;
  }
  .card-front {
    background: var(--card-white);
    display: flex;
    flex-direction: column;
    align-items: center;
  }
  .brand-lockup {
    display: flex;
    align-items: center;
    gap: 14px;
  }
  .brand-square {
    width: 34px;
    height: 34px;
    flex: none;
  }
  .brand-name {
    font-family: "Open Sans", Arial, sans-serif;
    font-weight: 700;
    font-size: 38px;
    line-height: 1.05;
    letter-spacing: -0.5px;
    text-align: left;
  }
  .brand-name span { display: block; }
  .card-front .brand-lockup { margin-top: 150px; }
  .card-front .brand-name { color: var(--brand-green); }
  .card-front .brand-square { background: var(--brand-green); }
  .brand-rule {
    width: 70px;
    height: 1px;
    background: var(--rule-grey);
    margin-top: 20px;
  }
  .holder-name {
    margin-top: 118px;
    color: var(--brand-green);
    font-size: 31px;
    font-weight: 500;
    letter-spacing: -0.3px;
  }
  .contact-icons {
    display: flex;
    align-items: center;
    gap: 6px;
    margin-top: 16px;
  }
  .contact-icons .rule { width: 40px; height: 1px; background: var(--ink-grey); margin: 0 6px; }
  .icon-tile {
    width: 24px; height: 24px;
    border-radius: 5px;
    background: var(--brand-green);
    display: flex; align-items: center; justify-content: center;
  }
  .contact-list {
    list-style: none;
    text-align: center;
    color: var(--ink-grey);
    font-size: 18px;
    line-height: 1.2;
    margin-top: 4px;
  }
  .card-back { background: var(--brand-green); }
  .back-pattern {
    position: absolute;
    inset: 0;
    background: linear-gradient(170deg, var(--brand-green-light) 0%, var(--brand-green) 70%);
  }
  .card-back .brand-block {
    position: absolute;
    left: 0; right: 0;
    bottom: 100px;
    display: flex;
    flex-direction: column;
    align-items: center;
  }
  .card-back .brand-name { color: var(--card-white); }
  .card-back .brand-square { background: var(--card-white); }
  .card-back .brand-rule { background: rgba(255,255,255,0.45); }
</style>
</head>
<body>
  <section class="card card-front" aria-label="Business card front">
    <div class="brand-lockup">
      <span class="brand-square" aria-hidden="true"></span>
      <p class="brand-name"><span>tidewell</span><span>homecraft.</span></p>
    </div>
    <div class="brand-rule"></div>
    <h1 class="holder-name">Dorian Keswick</h1>
    <div class="contact-icons">
      <span class="rule"></span>
      <span class="icon-tile">
        <svg width="14" height="14" viewBox="0 0 24 24" aria-hidden="true"><path fill="#fff" d="M6.6 10.8a15 15 0 0 0 6.6 6.6l2.2-2.2a1 1 0 0 1 1-.25 11.4 11.4 0 0 0 3.6.57 1 1 0 0 1 1 1V20a1 1 0 0 1-1 1A17 17 0 0 1 3 4a1 1 0 0 1 1-1h3.5a1 1 0 0 1 1 1c0 1.25.2 2.45.57 3.57a1 1 0 0 1-.25 1z"/></svg>
      </span>
      <span class="icon-tile">
        <svg width="14" height="14" viewBox="0 0 24 24" aria-hidden="true"><rect x="2" y="5" width="20" height="14" rx="1.5" fill="none" stroke="#fff" stroke-width="2"/><path d="M3 6l9 7 9-7" fill="none" stroke="#fff" stroke-width="2"/></svg>
      </span>
      <span class="icon-tile">
        <svg width="14" height="14" viewBox="0 0 24 24" aria-hidden="true"><circle cx="12" cy="12" r="9" fill="none" stroke="#fff" stroke-width="2"/><ellipse cx="12" cy="12" rx="4" ry="9" fill="none" stroke="#fff" stroke-width="1.6"/><path d="M3 12h18" stroke="#fff" stroke-width="1.6"/></svg>
      </span>
      <span class="rule"></span>
    </div>
    <ul class="contact-list">
      <li>0217392604</li>
      <li>dkeswick@tidewellhomecraft.co.nz</li>
      <li>www.tidewellhomecraft.co.nz</li>
    </ul>
  </section>

  <section class="card card-back" aria-label="Business card back">
    <div class="back-pattern" role="img" aria-label="Faint tonal repeat of the brand mark across the green background"></div>
    <div class="brand-block">
      <div class="brand-lockup">
        <span class="brand-square" aria-hidden="true"></span>
        <p class="brand-name"><span>tidewell</span><span>homecraft.</span></p>
      </div>
      <div class="brand-rule"></div>
    </div>
  </section>
</body>
</html>
```